Web Site Design

We need to design the whole web site for our small start up. We sell hospitality and culinary art internships abroad. I did my own design with WIX which is horrible meanwhile I started with my business. You can see it www.brindle-passage.org I will need you to create a new and attractive web site and to leave it working on wix. The internship destinations are United Arab Emirates, Thailand, China, Spain, Brazil and maybe leave a couple of pages for future destinations.You could also get other ideas of other sites that do internships.

Target Market(s)

Students and recent graduates of hospitality and culinary art majors

Industry/Entity Type

Education

Number of Pages Required

5+ page

Requirements
Must have
• Addittional to our program destinations, or to the pages in the current site. The website must contain a page for Universities or Hotels who require our service

```html
<!DOCTYPE html>
<html lang="en">
<head>
<meta charset="utf-8">
<title>Brindle Passage — Hospitality Internships Abroad</title>
<link rel="stylesheet" href="https://fonts.googleapis.com/css2?family=Marcellus&family=Crimson+Text:wght@400;600;700&display=swap">
<style>
:root{
  --teal:#2b8080;
  --teal-dark:#226b6b;
  --ink:#1c1c1c;
  --text:#333;
  --muted:#777;
  --header:#151515;
  --footer:#1f1f1f;
  --footer-bar:#111;
  --light:#f2f2f2;
  --white:#fff;
  --orange:#e0762b;
  --red:#c0392b;
}
*{box-sizing:border-box;margin:0;padding:0}
html,body{width:1200px;height:4369px;overflow:hidden}
body{font-family:"Crimson Text",Georgia,serif;color:var(--text);background:var(--white);position:relative}
.heading{font-family:"Marcellus",Georgia,serif;font-weight:400}
.btn{display:inline-block;background:var(--teal);color:var(--white);font-size:15px;padding:6px 26px;border-radius:16px;text-decoration:none}
.btn-white{background:var(--white);color:var(--teal)}
section,header,footer{position:absolute;left:0;width:1200px}

/* header */
.site-header{top:0;height:160px;background:var(--header);color:#ddd}
.topbar{height:34px;border-bottom:1px solid #333;display:flex;align-items:center;padding:0 120px;font-size:13px;justify-content:space-between}
.topbar .mid{position:absolute;left:490px}
.topbar .account span{margin-left:20px}
.logo{position:absolute;left:120px;top:48px;display:flex;align-items:center;gap:10px;color:var(--white)}
.logo .mark{width:46px;height:46px;border:2px solid var(--white);border-radius:50%}
.logo .name{font-size:18px;line-height:1.05;text-transform:uppercase}
.nav{position:absolute;right:120px;top:86px;display:flex;gap:30px;font-size:15px;align-items:center}
.nav a{color:#ddd;text-decoration:none;padding-bottom:6px}
.nav a.active{color:var(--teal);border-bottom:2px solid var(--teal)}

/* hero */
.hero{top:160px;height:612px}
.hero .photo{position:absolute;inset:0;background:linear-gradient(120deg,#7a6d62,#c9bfb5 45%,#8d9aa4 75%,#5d6770)}
.hero .shade{position:absolute;inset:0;background:rgba(0,0,0,.18)}
.hero .caption{position:absolute;left:0;right:0;top:270px;text-align:center;color:var(--white)}
.hero h1{font-size:38px;letter-spacing:1px}
.hero p{font-size:17px;margin:10px 0 18px}
.arrow{position:absolute;width:30px;height:30px;border-radius:50%;background:var(--white);display:flex;align-items:center;justify-content:center}
.hero .prev{left:38px;top:318px}.hero .next{right:38px;top:318px}
.dots{display:flex;gap:8px;justify-content:center}
.dots i{width:12px;height:12px;border-radius:50%;background:#ccc;display:block}
.dots i.on{background:var(--white);border:2px solid var(--teal)}
.hero .dots{position:absolute;bottom:52px;left:0;right:0}

/* about */
.about{top:772px;height:510px}
.about .copy{position:absolute;left:120px;top:92px;width:500px;font-size:16px;line-height:1.35}
.about h2{font-size:30px;color:var(--ink);margin-bottom:12px}
.about .copy p{margin-bottom:14px}
.about .program{font-size:20px;font-weight:700;color:var(--ink)}
.about .photo{position:absolute;left:632px;top:88px;width:448px;height:300px;background:linear-gradient(135deg,#c9c2b8,#8b8f95 60%,#3b3e45)}

/* destination */
.destination{top:1282px;height:591px;background:var(--teal);color:var(--white);text-align:center}
.section-title{font-size:32px;padding-top:42px}
.emblem{width:26px;height:26px;border:2px solid currentColor;border-radius:50%;margin:6px auto 4px}
.destination .sub{font-size:15px}
.pager{position:absolute;right:120px;top:48px;display:flex;gap:6px}
.pager span{width:24px;height:24px;border-radius:50%;background:var(--white);display:flex;align-items:center;justify-content:center}
.cards{position:absolute;left:120px;top:168px;display:flex;gap:15px}
.dest-card{width:230px;height:275px;background:var(--white);border-radius:10px;overflow:hidden;color:var(--text);text-align:left}
.dest-card .photo{height:152px}
.dest-card h3{font-size:17px;color:var(--teal);padding:6px 12px 2px;display:flex;justify-content:space-between;font-weight:600}
.dest-card h3 i{width:13px;height:13px;border:1.5px solid var(--teal);border-radius:50%}
.dest-card p{font-size:13px;line-height:1.25;padding:0 12px}
.dest-card .btn{display:block;margin:10px auto 0;width:100px;text-align:center;font-size:13px;padding:4px 0}
.view-all{position:absolute;left:527px;font-size:14px;padding:6px 0;width:146px;text-align:center}
.destination .view-all{top:495px}

/* testimonials */
.testimonials{top:1873px;height:609px;text-align:center}
.testimonials .section-title{color:var(--ink);font-size:28px;padding-top:108px}
.quotes{position:absolute;left:120px;top:190px;display:flex;gap:28px;align-items:flex-start}
.quote{width:278px;background:var(--light);padding:28px 20px 22px;font-size:14px;line-height:1.25}
.quote.featured{width:292px;background:var(--white);box-shadow:0 2px 10px rgba(0,0,0,.12);margin-top:-26px;padding:24px 30px 30px;font-size:15px}
.avatar{width:96px;height:96px;border-radius:50%;margin:0 auto 10px;background:linear-gradient(#d8d3cf,#8e8a86);border:3px solid var(--white)}
.quote .who{font-size:16px;color:var(--ink)}
.quote .role{color:var(--orange);font-size:13px;margin-bottom:4px}
.quote .more{font-size:13px;margin-top:8px}
.testimonials .dots{position:absolute;top:530px;left:0;right:0}
.testimonials .dots i{width:7px;height:7px;background:#555}

/* news */
.news{top:2482px;height:591px;background:var(--teal);color:var(--white);text-align:center}
.news .section-title{font-size:30px;padding-top:42px}
.news-grid{position:absolute;left:112px;top:128px;display:flex;gap:12px}
.news-card{width:324px;height:318px;background:var(--white);color:var(--text);text-align:left}
.news-card .photo{height:190px}
.news-card h3{font-size:15px;color:var(--ink);padding:10px 10px 0;font-weight:600}
.news-card .meta{font-size:11px;color:var(--muted);padding:0 10px}
.news-card p{font-size:14px;padding:4px 10px;line-height:1.2}
.news-card a{color:var(--red);font-size:13px;padding:0 10px;font-weight:600}
.news .view-all{top:505px}

/* interns */
.interns{top:3073px;height:487px;text-align:center}
.interns .section-title{color:var(--ink);font-size:28px;padding-top:80px}
.partner-grid{position:absolute;left:120px;top:157px;display:grid;grid-template-columns:repeat(5,180px);gap:16px 15px}
.partner{height:145px;background:var(--light);display:flex;align-items:center;justify-content:center;gap:6px;font-size:16px;color:var(--ink);font-weight:600}
.partner i{width:14px;height:14px;background:var(--teal)}

/* payments */
.payments{top:3560px;height:256px;text-align:center}
.payments .section-title{color:var(--ink);font-size:26px;padding-top:20px}
.fees{position:absolute;left:287px;top:72px;display:flex;gap:44px}
.fee{width:290px;height:140px;box-shadow:0 1px 6px rgba(0,0,0,.18);padding:14px}
.fee h3{font-size:19px;color:var(--ink);font-weight:600}
.cardset{display:flex;gap:4px;justify-content:center;margin:10px 0}
.cardset i{width:40px;height:26px;border-radius:3px;display:block}
.fee .btn{font-size:13px;padding:3px 28px}

/* newsletter */
.newsletter{top:3816px;height:198px;text-align:center}
.newsletter h2{font-size:30px;color:var(--ink)}
.newsletter p{font-size:16px;margin-top:2px;color:var(--ink)}
.signup{position:absolute;left:300px;top:96px;display:flex;align-items:center}
.signup .field{width:440px;border-bottom:1px solid #bbb;font-size:13px;color:var(--muted);text-align:left;padding:6px 4px}
.signup .btn{border-radius:16px;padding:6px 48px;font-weight:700}

/* footer */
.site-footer{top:4014px;height:312px;background:var(--footer);color:#ccc;font-size:14px}
.site-footer .logo{top:46px}
.site-footer .about-text{position:absolute;left:120px;top:140px;width:240px;line-height:1.2}
.site-footer .about-text a{color:#ccc;display:block;margin-top:4px}
.col{position:absolute;top:80px}
.col h4{font-size:13px;color:var(--white);letter-spacing:.5px;margin-bottom:14px;font-weight:700}
.col ul{list-style:none;line-height:1.85}
.col.links{left:388px}.col.links li::before{content:"• ";color:var(--white)}
.col.offices{left:545px}
.col.offices li{display:flex;align-items:center;gap:8px}
.col.offices li i{width:14px;height:10px;background:#888;display:block}
.col.contact{left:805px;width:275px}
.inputs{display:flex;gap:6px}
.inputs div,.msg{border:1px solid #555;background:#2a2a2a;font-size:12px;padding:5px 8px;flex:1}
.msg{height:54px;margin-top:8px}
.col.contact .btn{float:right;margin-top:10px;font-size:12px;padding:4px 34px}
.bottom-bar{position:absolute;left:0;width:1200px;top:4326px;height:43px;background:var(--footer-bar);color:#ccc;font-size:13px;display:flex;align-items:center;justify-content:space-between;padding:0 120px}
.social{display:flex;gap:8px}
.social i{width:22px;height:22px;border-radius:50%;background:var(--white);display:block}
</style>
</head>
<body>

<header class="site-header">
  <div class="topbar">
    <span>&#9742; +01 555 010 200</span>
    <span class="mid">&#9993; info@brindlepassage.org</span>
    <span class="account"><span>Login</span><span>Register</span></span>
  </div>
  <div class="logo"><span class="mark"></span><span class="name heading">Brindle<br>Passage</span></div>
  <nav class="nav">
    <a class="active" href="#">Home</a><a href="#">About us</a><a href="#">Distination</a><a href="#">Blogs</a><a href="#">Contact us</a>
    <svg width="12" height="12" viewBox="0 0 12 12"><circle cx="5" cy="5" r="3.5" fill="none" stroke="#ddd" stroke-width="1.4"/><line x1="7.6" y1="7.6" x2="11" y2="11" stroke="#ddd" stroke-width="1.4"/></svg>
  </nav>
</header>

<section class="hero">
  <div class="photo" role="img" aria-label="Team of chefs and hotel staff in a professional kitchen"></div>
  <div class="shade"></div>
  <div class="caption">
    <h1 class="heading">Hospitality Internship Program</h1>
    <p>Program : Culinary - F&amp;B - Front Office - Guest Relations</p>
    <a class="btn" href="#">Read More</a>
  </div>
  <span class="arrow prev"><svg width="10" height="12"><path d="M8 1 2 6l6 5" fill="none" stroke="#333" stroke-width="2"/></svg></span>
  <span class="arrow next"><svg width="10" height="12"><path d="M2 1l6 5-6 5" fill="none" stroke="#333" stroke-width="2"/></svg></span>
  <div class="dots"><i></i><i class="on"></i><i></i><i></i></div>
</section>

<section class="about">
  <div class="copy">
    <h2 class="heading">ABOUT US</h2>
    <p>Lorem Ipsum is simply dummy text of the printing and typesetting industry. Lorem Ipsum has been the industry's standard dummy text ever since the 1500s,</p>
    <p>when an unknown printer took a galley of type and scrambled it to make a type specimen book. It has survived not only five centuries</p>
    <div class="program">Program :</div>
    <p>Culinary - F&amp;B - Front Office - Guest Relations</p>
    <a class="btn" href="#">Read More</a>
  </div>
  <div class="photo" role="img" aria-label="Two hotel receptionists at a front desk with international flags"></div>
</section>

<section class="destination">
  <h2 class="section-title heading">Destination</h2>
  <div class="emblem"></div>
  <p class="sub">Lorem Ipsum is simply dummy text of the printing and typesetting.</p>
  <div class="pager"><span><svg width="8" height="10"><path d="M6 1 2 5l4 4" fill="none" stroke="#333" stroke-width="2"/></svg></span><span><svg width="8" height="10"><path d="M2 1l4 4-4 4" fill="none" stroke="#333" stroke-width="2"/></svg></span></div>
  <div class="cards">
    <article class="dest-card"><div class="photo" role="img" aria-label="Temple in China" style="background:linear-gradient(#9bb6cf,#6d5a48)"></div><h3>China<i></i></h3><p>Lorem Ipsum is simply dummy text of the printing and typesetting.</p><a class="btn" href="#">Details</a></article>
    <article class="dest-card"><div class="photo" role="img" aria-label="Evening city view in Spain" style="background:linear-gradient(#4a5a8a,#c2703c)"></div><h3>Spain<i></i></h3><p>Lorem Ipsum is simply dummy text of the printing and typesetting.</p><a class="btn" href="#">Details</a></article>
    <article class="dest-card"><div class="photo" role="img" aria-label="Harbour and opera house in Australia" style="background:linear-gradient(#6fa5d2,#2f5f88)"></div><h3>Australia<i></i></h3><p>Lorem Ipsum is simply dummy text of the printing and typesetting.</p><a class="btn" href="#">Details</a></article>
    <article class="dest-card"><div class="photo" role="img" aria-label="Glass museum pyramid at dusk in France" style="background:linear-gradient(#2c3f6b,#c99a4c)"></div><h3>France<i></i></h3><p>Lorem Ipsum is simply dummy text of the printing and typesetting.</p><a class="btn" href="#">Details</a></article>
  </div>
  <a class="btn btn-white view-all" href="#">View All</a>
</section>

<section class="testimonials">
  <h2 class="section-title heading">Testimonials</h2>
  <div class="quotes">
    <article class="quote"><div class="avatar" role="img" aria-label="Portrait of a student"></div><div class="who">Daniel Marsh</div><div class="role">Creative Director</div><p>Lorem Ipsum is simply dummy text of the printing and typesetting Lorem Ipsum industry.</p><div class="more">Read More...</div></article>
    <article class="quote featured"><div class="avatar" role="img" aria-label="Portrait of a student"></div><div class="who">Daniel Marsh</div><div class="role">Creative Director</div><p>“ Lorem Ipsum is simply dummy text of the printing and typesetting Lorem Ipsum industry. ”</p><div class="more">Read More...</div></article>
    <article class="quote"><div class="avatar" role="img" aria-label="Portrait of a student"></div><div class="who">Daniel Marsh</div><div class="role">Creative Director</div><p>Lorem Ipsum is simply dummy text of the printing and typesetting Lorem Ipsum industry.</p><div class="more">Read More...</div></article>
  </div>
  <div class="dots"><i></i><i></i><i></i></div>
</section>

<section class="news">
  <h2 class="section-title heading">Latest News</h2>
  <div class="pager"><span><svg width="8" height="10"><path d="M6 1 2 5l4 4" fill="none" stroke="#333" stroke-width="2"/></svg></span><span><svg width="8" height="10"><path d="M2 1l4 4-4 4" fill="none" stroke="#333" stroke-width="2"/></svg></span></div>
  <div class="news-grid">
    <article class="news-card"><div class="photo" role="img" aria-label="Hotel staff in uniform standing in a lobby" style="background:linear-gradient(#b9c3cc,#3c4048)"></div><h3>NEWS #1</h3><div class="meta">Sep 9, 2016 &nbsp; Comments (12)</div><p>Lorem Ipsum is simply dummy text of the printing and typesetting.</p><a href="#">Read More</a></article>
    <article class="news-card"><div class="photo" role="img" aria-label="Modern hotel lobby" style="background:linear-gradient(#d4d0c6,#6f6a60)"></div><h3>NEWS #1</h3><div class="meta">Sep 9, 2016 &nbsp; Comments (12)</div><p>Lorem Ipsum is simply dummy text of the printing and typesetting.</p><a href="#">Read More</a></article>
    <article class="news-card"><div class="photo" role="img" aria-label="Bright hotel room interior" style="background:linear-gradient(#e3e1dc,#8b8276)"></div><h3>NEWS #1</h3><div class="meta">Sep 9, 2016 &nbsp; Comments (12)</div><p>Lorem Ipsum is simply dummy text of the printing and typesetting.</p><a href="#">Read More</a></article>
  </div>
  <a class="btn btn-white view-all" href="#">View All</a>
</section>

<section class="interns">
  <h2 class="section-title heading">Previous Interns</h2>
  <div class="partner-grid">
    <div class="partner"><i></i>Larkfield</div>
    <div class="partner"><i></i>Orchard Row</div>
    <div class="partner"><i></i>Tidewell</div>
    <div class="partner"><i></i>Quillstone</div>
    <div class="partner"><i></i>Amberlee</div>
    <div class="partner"><i></i>Fernhollow</div>
    <div class="partner"><i></i>Copperbay</div>
    <div class="partner"><i></i>Wrenmoor</div>
    <div class="partner"><i></i>Lindholt</div>
    <div class="partner"><i></i>Vellamy</div>
  </div>
</section>

<section class="payments">
  <h2 class="section-title heading">Payments</h2>
  <div class="fees">
    <div class="fee"><h3>Enrollment Fee</h3><div class="cardset"><i style="background:#2b4f9e"></i><i style="background:#d8452f"></i><i style="background:#e08a2a"></i><i style="background:#3d8fd1"></i><i style="background:#1f3f8a"></i></div><a class="btn" href="#">Buy Now</a></div>
    <div class="fee"><h3>Program Fee</h3><div class="cardset"><i style="background:#2b4f9e"></i><i style="background:#d8452f"></i><i style="background:#e08a2a"></i><i style="background:#3d8fd1"></i><i style="background:#1f3f8a"></i></div><a class="btn" href="#">Buy Now</a></div>
  </div>
</section>

<section class="newsletter">
  <h2 class="heading">Subscribe to Our Newsletter</h2>
  <p>to receive the latest news &amp; update</p>
  <div class="signup"><div class="field">Your Email</div><a class="btn" href="#">Submit</a></div>
</section>

<footer class="site-footer">
  <div class="logo"><span class="mark"></span><span class="name heading">Brindle<br>Passage</span></div>
  <div class="about-text">Lorem Ipsum is simply dummy text of the printing and typesetting Lorem Ipsum industry.<a href="#">Read More...</a></div>
  <div class="col links"><h4>QUICK LINK</h4><ul><li>Home</li><li>About us</li><li>Distination</li><li>Blogs</li><li>Contact us</li></ul></div>
  <div class="col offices"><h4>OUR OFFICES</h4><ul>
    <li><i></i>Mexico : 52 55 0100 4410</li>
    <li><i></i>United States : 1 555-014-2267</li>
    <li><i></i>Europe : 35 7 0100 5582</li>
    <li><i></i>Australia : 61 400 555 018</li>
    <li><i></i>Email : Australia : 61 400 555 018</li>
  </ul></div>
  <div class="col contact"><h4>QUICK CONTACT</h4>
    <div class="inputs"><div>Name</div><div>Phone</div></div>
    <div class="msg">Message</div>
    <a class="btn" href="#">SEND</a>
  </div>
</footer>
<div class="bottom-bar">
  <span>Copyright 2018 Brindle Passage, All Rights Reserved.</span>
  <span class="social"><i></i><i></i><i></i><i></i><i></i></span>
</div>

</body>
</html>
```